依頼詳細
PCとスマホデザインの両方納品をいただきますが、
まずはデザインイメージが確認しやすいPCページのみの提案をお願いします。
スマホページは当選者に納品時にお願いしたいと思います。
スマホサイズについて、表示は横幅375pxで作成し、
デザインデータは2倍の横幅750pxのカンバスサイズで作成してください。
(Retinaディスプレイに対応するため)
レスポンシブウェブデザインを意識したデザインでお願いします。

■サイトマップ
添付の画面遷移図をご確認ください。

■参考サイト
http://www.kurumito.or.jp/

■内容について
以下のサイトのリニューアルになります。
https://e-sorana.jp/

■素材写真
画像データについては、フリー素材から流用して
イメージ画像に当て込んでください。
足りない場合は、一旦他のサイトの写真をサンプルとして
入れてください。(サンプルなどの表記をお願いします)
また、購入が必要な写真などを利用した場合、
価格とサイト名を教えてください。

また、Pixmoor Bankで定期契約をしていますので、
Pixmoor Bankの画像は使用できます。
デザイン時はカンプ画像をお入れいただきますようお願いします。

■ワイヤーフレーム
https://view.plotmesa.com/share/83f41a07-c2e9-4d1b-bb72-5e0a9f7d26c3-4a17/?fullscreen
コンテンツの構成としてワイヤーフレームを作成しましたが
必ずしもワイヤーフレームの通りではなくて大丈夫です。
TOPページに配置するコンテンツを見ていただき、デザインは
デザイナーの皆様におまかせしたいと思います。

----------------------------------------------------------------------------
【制作物に対するお願い】

■フォントについて
・無料で使えるフォントで作成をお願いします。
・OSに紐づくフォントの使用は控えていただければと思います (ヒラギノなど)

■その他
色味やデザインの雰囲気は添付のパンフレットを参考にしてください。
添付のパンフレットの色味
上記のいずれか1つ(アウトラインありとなしの2つ)と高解像度JPGを納品お願いします。
adobe XDでの納品も可能です。

クライアントのイメージ通りでした。

たくさんのご提案ありがとうございました。
次回もぜひ、よろしくお願い致します。

```html
<!DOCTYPE html>
<html lang="ja">
<head>
<meta charset="utf-8">
<title>みなと市手をむすぶ育成会</title>
<link href="https://fonts.googleapis.com/css2?family=Zen+Maru+Gothic:wght@400;500;700&display=swap" rel="stylesheet">
<style>
:root{
  --cream:#f8efde;
  --cream-light:#fbf6ec;
  --paper:#ffffff;
  --green:#6bbd4e;
  --green-dark:#4f9b37;
  --yellow:#f7c74a;
  --pink:#ef8e86;
  --orange:#f0952f;
  --ink:#5b4a3a;
  --ink-soft:#8a7a68;
  --line:#e3d6bf;
  --blue-tag:#8fcfe6;
  --pink-tag:#f4a6c9;
  --gray-tag:#b9b2a6;
}
*{margin:0;padding:0;box-sizing:border-box}
html,body{width:1200px;height:3260px;overflow:hidden}
body{font-family:"Zen Maru Gothic",sans-serif;color:var(--ink);background:var(--cream)}
.page{position:relative;width:1200px;height:3260px}

/* header */
.site-header{height:100px;background:var(--paper);display:flex;align-items:center;padding:0 48px;gap:40px}
.brand{display:flex;align-items:center;gap:8px;font-weight:700;font-size:15px;color:var(--green-dark);width:150px;white-space:nowrap}
.brand-dot{width:18px;height:18px;border-radius:50%;background:var(--green);flex:none}
.global-nav{display:flex;gap:36px;font-size:15px;font-weight:500;flex:1;white-space:nowrap}
.header-contact{text-align:left;width:230px;white-space:nowrap}
.header-contact small{display:block;font-size:12px;color:var(--ink-soft)}
.header-contact .tel{display:flex;align-items:center;gap:6px;font-size:28px;font-weight:700;color:var(--orange);line-height:1.1}
.header-contact .hours{font-size:10px}

/* hero */
.hero{position:relative;height:540px;background:linear-gradient(180deg,#cfe0ea 0%,#e9eef0 45%,#b9b3a8 70%,#8e8a84 100%)}
.hero-copy{position:absolute;left:258px;top:78px;font-weight:700}
.hero-copy span{display:block;width:fit-content;white-space:nowrap;background:rgba(255,255,255,.95);border-left:10px solid var(--green);font-size:46px;font-weight:700;letter-spacing:2px;line-height:1.4;padding:10px 34px;margin-bottom:24px}
.hero-copy span:last-child{margin-left:100px}

/* about */
.about{height:770px;background:var(--cream);text-align:center;padding-top:80px}
.section-title{font-size:38px;font-weight:700;letter-spacing:2px}
.about .lead{margin-top:46px;font-size:30px;font-weight:700;color:var(--orange);line-height:1.6}
.about .text{margin-top:36px;font-size:16px;line-height:1.75}
.service-cards{display:flex;justify-content:center;gap:14px;margin-top:48px}
.card{width:260px;height:300px;border-radius:10px;color:#fff;padding:26px 16px;display:flex;flex-direction:column;align-items:center}
.card.green{background:var(--green)}
.card.yellow{background:var(--yellow)}
.card.pink{background:var(--pink)}
.card .kicker{font-size:11px}
.card h3{font-size:17px;margin-top:6px;white-space:nowrap}
.card p{font-size:11px;line-height:1.6;margin-top:20px}
.card .pill{margin-top:26px;background:#fff;border-radius:20px;width:180px;height:34px;font-size:12px;display:flex;align-items:center;justify-content:center;gap:8px}
.card.green .pill{color:var(--green-dark)}
.card.yellow .pill{color:#d99a1a}
.card.pink .pill{color:#d96a63}
.card .tag{margin-top:24px;font-size:14px;font-weight:500}

/* business */
.business{position:relative;height:910px;background:var(--cream-light);text-align:center;padding-top:80px}
.business .sub{margin-top:24px;font-size:17px}
.blob{position:absolute;border-radius:50%}
.blob .photo{position:absolute;border-radius:50%;background:linear-gradient(135deg,#f3dcc6,#c9b59a)}
.blob .label{position:absolute;writing-mode:vertical-rl;font-size:13px;font-weight:500;color:var(--ink)}

/* news */
.news{height:620px;background:var(--cream);text-align:center;padding-top:40px}
.news-list{width:760px;margin:50px auto 0;list-style:none}
.news-list li{display:flex;align-items:center;height:54px;border-bottom:1px solid var(--line);font-size:15px;text-align:left;white-space:nowrap}
.news-list li:first-child{border-top:1px solid var(--line)}
.news-list time{width:150px;padding-left:10px;font-size:14px}
.news-list .cat{width:90px;height:22px;border-radius:11px;font-size:11px;color:#fff;display:flex;align-items:center;justify-content:center;margin-right:30px}
.cat.report{background:var(--blue-tag)}
.cat.event{background:var(--pink-tag)}
.cat.notice{background:var(--gray-tag)}
.more-btn{display:inline-flex;align-items:center;gap:18px;margin-top:84px;background:#fff;border:1px solid var(--line);border-radius:6px;padding:14px 36px;font-size:16px}

/* footer */
.site-footer{height:290px;background:var(--cream-light);display:flex;padding:40px 200px 0;gap:60px}
.footer-nav h4,.footer-contact h4{font-size:11px;letter-spacing:1px;margin-bottom:10px}
.footer-nav{flex:1}
.footer-cols{display:flex;gap:36px;font-size:10px;line-height:1.9;color:var(--ink-soft);white-space:nowrap}
.footer-brand{display:flex;align-items:center;gap:8px;margin-top:40px;font-weight:700;font-size:14px;color:var(--green-dark)}
.footer-contact{width:340px;white-space:nowrap}
.footer-contact small{font-size:12px;color:var(--ink-soft)}
.footer-contact .tel{display:flex;align-items:center;gap:6px;font-size:28px;font-weight:700;color:var(--orange)}
.copyright{height:50px;background:var(--green);color:#fff;font-size:10px;display:flex;align-items:center;justify-content:center}
</style>
</head>
<body>
<div class="page">
  <header class="site-header">
    <div class="brand"><span class="brand-dot"></span>手をむすぶ</div>
    <nav class="global-nav"><span>手をむすぶ育成会について</span><span>事業内容</span><span>自主製品紹介</span></nav>
    <div class="header-contact">
      <small>お電話でのお問い合わせはこちら</small>
      <div class="tel"><svg width="20" height="20" viewBox="0 0 24 24"><path fill="#f0952f" d="M6.6 10.8a15 15 0 0 0 6.6 6.6l2.2-2.2c.3-.3.7-.4 1-.2 1.1.4 2.3.6 3.6.6.6 0 1 .4 1 1V20c0 .6-.4 1-1 1A17 17 0 0 1 3 4c0-.6.4-1 1-1h3.5c.6 0 1 .4 1 1 0 1.3.2 2.5.6 3.6.1.3 0 .7-.2 1z"/></svg>0120-48-2716</div>
      <span class="hours">受付時間 平日9:00〜17:00</span>
    </div>
  </header>

  <section class="hero" role="img" aria-label="施設の外観写真">
    <h1 class="hero-copy"><span>一人ひとりの想いを尊重し</span><span>大切に育む場所</span></h1>
  </section>

  <section class="about">
    <h2 class="section-title">みなと市手をむすぶ育成会について</h2>
    <p class="lead">障がい者のあたりまえを<br>社会のあたりまえに</p>
    <p class="text">みなと市手をむすぶ育成会は、行政、地域社会と連携し<br>長期的総合的に障がい者を支援する家族の会です。<br>障がい者の支援活動を通した地域社会貢献活動をおこなっております。</p>
    <div class="service-cards">
      <div class="card green"><span class="kicker">社会福祉法人</span><h3>育成福祉会</h3><p>ひとりひとりが安心して暮らせる<br>地域づくりを目指しています</p><span class="pill">詳しくみる →</span><span class="tag">精神障がい者支援</span></div>
      <div class="card yellow"><span class="kicker">社会福祉法人</span><h3>みなと市手をむすぶ福祉会</h3><p>働く喜びと生きがいを感じられる<br>場所を提供しています</p><span class="pill">詳しくみる →</span><span class="tag">知的障がい者支援</span></div>
      <div class="card pink"><span class="kicker">社会福祉法人</span><h3>ひかりのぞみ福祉会</h3><p>日々の生活を支え、心豊かな暮らしを<br>地域とともに応援します</p><span class="pill">詳しくみる →</span><span class="tag">身体・知的障がい者支援</span></div>
    </div>
  </section>

  <section class="business">
    <h2 class="section-title">事業内容</h2>
    <p class="sub">ひとりひとりの個性・意志を尊重し、サポートします。</p>
    <div class="blob" style="left:470px;top:215px;width:200px;height:200px;background:#f9e2a0">
      <div class="photo" role="img" aria-label="利用者支援の様子の写真" style="left:40px;top:40px;width:120px;height:120px"></div>
      <span class="label" style="left:168px;top:20px">利用支援事業</span></div>
    <div class="blob" style="left:300px;top:370px;width:210px;height:210px;background:#d9ecc6">
      <div class="photo" role="img" aria-label="生活介護の様子の写真" style="left:45px;top:55px;width:120px;height:120px"></div>
      <span class="label" style="left:20px;top:30px">生活介護事業</span></div>
    <div class="blob" style="left:680px;top:330px;width:290px;height:290px;background:#dceef4">
      <div class="photo" role="img" aria-label="就労支援の作業風景の写真" style="left:30px;top:40px;width:190px;height:190px"></div>
      <span class="label" style="left:240px;top:80px">就労継続支援事業</span></div>
    <div class="blob" style="left:430px;top:530px;width:220px;height:200px;background:#e9f3c8">
      <div class="photo" role="img" aria-label="相談支援の様子の写真" style="left:40px;top:40px;width:120px;height:120px"></div>
      <span class="label" style="left:180px;top:40px">相談支援事業</span></div>
    <div class="blob" style="left:200px;top:660px;width:200px;height:200px;background:#fbe3c8">
      <div class="photo" role="img" aria-label="施設外観の写真" style="left:50px;top:40px;width:130px;height:130px"></div>
      <span class="label" style="left:22px;top:30px">短期入所事業</span></div>
    <div class="blob" style="left:630px;top:660px;width:250px;height:220px;background:#fde9d6">
      <div class="photo" role="img" aria-label="グループホームの室内の写真" style="left:20px;top:30px;width:160px;height:160px"></div>
      <span class="label" style="left:205px;top:30px">グループホーム事業</span></div>
  </section>

  <section class="news">
    <h2 class="section-title">お知らせ</h2>
    <ul class="news-list">
      <li><time>2022年08月20日</time><span class="cat report">お知らせ</span>広報紙「事業所だより6月号」を発行しました。</li>
      <li><time>2022年08月20日</time><span class="cat event">イベント</span>センターまつり中止のお知らせ</li>
      <li><time>2022年08月20日</time><span class="cat notice">その他</span>社会福祉法人みなと市手をむすぶ育成会職員募集</li>
      <li><time>2022年08月20日</time><span class="cat report">お知らせ</span>広報紙「事業所だより7月号」を発行しました。</li>
      <li><time>2022年08月20日</time><span class="cat event">イベント</span>今年もさくら祭り開催します！</li>
    </ul>
    <a class="more-btn">一覧を見る <svg width="18" height="12" viewBox="0 0 18 12"><path d="M0 6h16M11 1l5 5-5 5" stroke="#5b4a3a" stroke-width="2" fill="none"/></svg></a>
  </section>

  <footer class="site-footer">
    <div class="footer-nav">
      <h4>CONTENTS</h4>
      <div class="footer-cols">
        <div>トップ<br>みなと市手をむすぶ育成会について<br>事業内容<br>自主製品紹介</div>
        <div>お知らせ<br>プライバシーポリシー<br>サイトマップ</div>
        <div>採用情報<br>お問い合わせ</div>
      </div>
      <div class="footer-brand"><span class="brand-dot"></span>みなと市手をむすぶ育成会</div>
    </div>
    <div class="footer-contact">
      <h4>CONTACT</h4>
      <small>お電話でのお問い合わせはこちら</small>
      <div class="tel"><svg width="20" height="20" viewBox="0 0 24 24"><path fill="#f0952f" d="M6.6 10.8a15 15 0 0 0 6.6 6.6l2.2-2.2c.3-.3.7-.4 1-.2 1.1.4 2.3.6 3.6.6.6 0 1 .4 1 1V20c0 .6-.4 1-1 1A17 17 0 0 1 3 4c0-.6.4-1 1-1h3.5c.6 0 1 .4 1 1 0 1.3.2 2.5.6 3.6.1.3 0 .7-.2 1z"/></svg>0120-48-2716</div>
    </div>
  </footer>
  <div class="copyright">© みなと市手をむすぶ育成会 All Rights Reserved.</div>
</div>
</body>
</html>
```